Packaging and labelling for Swiss made Organic CBD Oil

Visit our website www.velmarotiva.com
We have not put any product on yet as require packaging and label design .
Website will give you a great feel for the company and how we have used
the logo . The Drevask cbd product shown is a company similar to ourselves with similar core values , we liked the clean packaging design they have .

Im happy if you want use the mandala symbol in our logo separate from
VELMARO, to separate and use the mandala symbol as a larger icon than
it appears in our logo
Clean , Pure , organic feel. Like the product to look pharmaceutical and life changing not gimmicky.
Colours to go with or be the same as our logo colours
But not too cold and clinical
Bottle size 84mm x 25mm
Label size 75mm x 30mm
Box 30mm x 30mm x 100mm
6 products
Full Spectrum :
500mg CBD (5%)
1000mg CBD ( 10% )
1500mg CBD (15%)
2000mg CBD ( 20% )
Broad spectrum THC Free
500mg CBD (5%)
Pets
500mg Broad Spectrum THC Free
Updates

Would like the design to be more modern than traditional

LABEL Information Front of Bottle - Logo VELMARO & Mandala - Mandala can be used separately as design symbol Organic Cannabis Oil 1500mg CBD (15%) Ful Spectrum 10ml Back of bottle Ingredients: Organic Cannabis Oil Extract Organic Sunflower Seed Oil THC - 0.2% Certified Swiss Organic Cultivation Shake well before use. Store in a cool , dry place and out of the each of children BOX information Front and rear Logo - VELMARO & Mandala - Mandala can be used separately as a design symbol Organic Cannabis Oil 1500mg CBD (15%) Full Spectrum Sides x 2 This product is a food supplement and is not intended to diagnose, treat, cure or prevent any disease If you are pregnant, lactating or taking any medication consult your health care practitioner Suitable for vegetarians and vegans Ingredients Organic Cannabis Oil extract Organis Sunflower Oil Store in a cool ,dry place, out of the reach of children Recommended Use 1-5 drops ( 1 drop = 7.5mg CBD ) Subject to body weight and personal requirement - visit www.velmarotiva for more information 100% Natural 100% Organic GMO free 100% Vegan ( symbol with each ) Expiry date see bottle label Cultivated and manufactured in Switzerland

Target Market(s)

age 40 - 80

Font styles to use
Other font styles liked:
• In our website we have used Open Sans for the copy and Lato for headings .

Requirements
Must have
• look like an Industry leader
Velmaro will change the quality of peoples lives and in some cases may
even save lives so want look powerful and credible
Our Mission is - Through Delivering Pure , Premium , Organic products we will educate, inform and help people achieve healthier , happier lifestyles
Nice to have
• Colours to look good with our logo colours or be the same as our logo
colours
Logo Font - Avenir Black and Avenir Book

Font used in website - Content - Open Sans / Headings - Lato
If you have another font for the packaging information that will go well with
our logo, I'm happy for you to use your skills

```html
<!DOCTYPE html>
<html lang="en">
<head>
<meta charset="utf-8">
<title>Velmaro Organic Cannabis Oil – Label and Box Dieline</title>
<link href="https://fonts.googleapis.com/css2?family=Lexend:wght@300&family=Open+Sans:wght@400;600;700;800&display=swap" rel="stylesheet">
<style>
  :root {
    --ink-grey: #8b8c8d;
    --soft-grey: #9a9b9c;
    --teal: #8fd6d6;
    --teal-tint: #e9f6f6;
    --cut-line: #b4b4b4;
    --fold-guide: #4fe3e8;
    --paper: #ffffff;
  }
  * { margin: 0; padding: 0; box-sizing: border-box; }
  html, body { width: 1200px; height: 1000px; overflow: hidden; background: var(--paper); }
  body { position: relative; font-family: "Open Sans", sans-serif; color: var(--ink-grey); }

  .panel { position: absolute; border: 1px solid var(--cut-line); background: var(--paper); }
  .fold-guide { position: absolute; width: 1px; background: var(--fold-guide); top: 11px; height: 952px; }
  .panel-divider { position: absolute; width: 1px; background: var(--cut-line); }

  .brand {
    position: absolute; display: flex; align-items: center; gap: 5px;
    font-family: "Open Sans", sans-serif; font-weight: 800; color: var(--ink-grey);
    letter-spacing: 0.06em; line-height: 1;
  }
  .brand-dot { width: 8px; height: 8px; border-radius: 50%; background: var(--teal); }

  .headline {
    position: absolute; text-align: center; font-family: "Lexend", sans-serif; font-weight: 300;
    color: var(--ink-grey); letter-spacing: 0.04em; line-height: 1.02;
  }
  .strength {
    position: absolute; text-align: center; font-family: "Lexend", sans-serif; font-weight: 300;
    color: var(--ink-grey); line-height: 1.15;
  }
  .spectrum-tag {
    position: absolute; background: var(--teal-tint); text-align: center;
    font-family: "Lexend", sans-serif; font-weight: 300; color: var(--ink-grey); line-height: 1;
    display: flex; align-items: center; justify-content: center; letter-spacing: 0.02em;
  }
  .volume { position: absolute; text-align: center; font-family: "Lexend", sans-serif; font-weight: 300; font-size: 13px; }

  .info-copy {
    position: absolute; text-align: center; font-size: 9.6px; line-height: 12.3px; color: var(--soft-grey);
  }
  .info-copy p + p { margin-top: 12.3px; }
  .info-copy .label { font-weight: 600; color: var(--soft-grey); }
  .info-copy .accent { color: var(--teal); }
  .info-copy .heading { font-weight: 600; color: var(--teal); }

  .badge { position: absolute; width: 60px; text-align: center; }
  .badge-ring { display: block; margin: 0 auto; }
  .badge-name { display: block; margin-top: 3px; font-size: 9.6px; font-weight: 600; color: var(--teal); white-space: nowrap; margin-left: -20px; margin-right: -20px; }

  .lid-mark {
    position: absolute; left: 706px; top: 21px; width: 342px; height: 342px;
    display: flex; align-items: center; justify-content: center; gap: 8px;
    font-weight: 800; font-size: 26px; letter-spacing: 0.08em; color: var(--teal);
  }
  .lid-mark .brand-dot { width: 14px; height: 14px; }
</style>
</head>
<body>

  <!-- Bottle label -->
  <div class="panel bottle-label" style="left:113px; top:467px; width:171px; height:428px;"></div>
  <div class="brand" style="left:131px; top:511px; font-size:22px;"><span class="brand-dot"></span>VELMARO</div>
  <div class="headline" style="left:113px; top:638px; width:171px; font-size:27px;">ORGANIC<br>CANNABIS<br>OIL</div>
  <div class="strength" style="left:113px; top:763px; width:171px; font-size:18px;">1500 mg<br>CBD (5%)</div>
  <div class="spectrum-tag" style="left:130px; top:824px; width:136px; height:20px; font-size:17px;">Full Spectrum</div>
  <div class="volume" style="left:113px; top:874px; width:171px;">10 ml</div>

  <!-- Box lid -->
  <div class="panel box-lid" style="left:706px; top:21px; width:342px; height:342px;"></div>
  <div class="lid-mark"><span class="brand-dot"></span>VELMARO</div>

  <!-- Box body -->
  <div class="panel box-body" style="left:363px; top:381px; width:685px; height:571px;"></div>
  <div class="panel-divider" style="left:706px; top:381px; height:571px;"></div>

  <!-- Front panel -->
  <div class="brand" style="left:376px; top:434px; font-size:21px;"><span class="brand-dot"></span>VELMARO</div>
  <div class="headline" style="left:363px; top:653px; width:172px; font-size:21px;">ORGANIC<br>CANNABIS<br>OIL</div>
  <div class="strength" style="left:363px; top:793px; width:172px; font-size:19px;">1500 mg<br>CBD (5%)</div>
  <div class="spectrum-tag" style="left:389px; top:909px; width:118px; height:18px; font-size:15px;">Full Spectrum</div>

  <!-- Side panel: advisory -->
  <div class="info-copy" style="left:540px; top:731px; width:162px;">
    <p>This product is a food<br>supplement and is not intended<br>to diagnose, treat, cure or<br>prevent any disease.</p>
    <p>If you are pregnant, lactating or<br>taking any medication consult<br>your health care practitioner.</p>
    <p>Suitable for vegetarians<br>and vegans.</p>
    <p><span class="label">Ingredients:</span> <span class="accent">Organic Cannabis</span><br>Oil Extract Organic Sunflower<br>Oil Store in a cool, dry place, out<br>of the reach of children.</p>
  </div>

  <!-- Rear panel -->
  <div class="brand" style="left:720px; top:434px; font-size:21px;"><span class="brand-dot"></span>VELMARO</div>
  <div class="headline" style="left:706px; top:653px; width:170px; font-size:21px;">ORGANIC<br>CANNABIS<br>OIL</div>
  <div class="strength" style="left:706px; top:793px; width:170px; font-size:19px;">1500 mg<br>CBD (5%)</div>
  <div class="spectrum-tag" style="left:733px; top:909px; width:118px; height:18px; font-size:15px;">Full Spectrum</div>

  <!-- Side panel: usage and claims -->
  <div class="info-copy" style="left:880px; top:432px; width:164px;">
    <p><span class="heading">Recommended Use:</span><br>1-5 drops (1 drop = 7.5mg CBD)<br>Subject to body weight and<br>personal requirement – visit<br>www.velmarotiva.com<br>for more information.</p>
  </div>

  <div class="badge" style="left:931px; top:529px;">
    <svg class="badge-ring" width="54" height="54" viewBox="0 0 54 54"><circle cx="27" cy="27" r="25" fill="none" stroke="var(--teal)" stroke-width="2.5"/><circle cx="27" cy="27" r="9" fill="var(--teal)"/></svg>
    <span class="badge-name">100% Natural</span>
  </div>
  <div class="badge" style="left:931px; top:614px;">
    <svg class="badge-ring" width="54" height="54" viewBox="0 0 54 54"><circle cx="27" cy="27" r="25" fill="none" stroke="var(--teal)" stroke-width="2.5"/><circle cx="27" cy="27" r="9" fill="var(--teal)"/></svg>
    <span class="badge-name">100% Organic</span>
  </div>
  <div class="badge" style="left:931px; top:703px;">
    <svg class="badge-ring" width="54" height="54" viewBox="0 0 54 54"><circle cx="27" cy="27" r="25" fill="none" stroke="var(--teal)" stroke-width="2.5"/><circle cx="27" cy="27" r="9" fill="var(--teal)"/></svg>
    <span class="badge-name">100% Vegan</span>
  </div>
  <div class="badge" style="left:931px; top:791px;">
    <svg class="badge-ring" width="54" height="54" viewBox="0 0 54 54"><circle cx="27" cy="27" r="25" fill="none" stroke="var(--teal)" stroke-width="2.5"/><circle cx="27" cy="27" r="9" fill="var(--teal)"/></svg>
    <span class="badge-name">GMO Free</span>
  </div>

  <div class="info-copy" style="left:880px; top:883px; width:164px;">
    <p>Expiry date see bottle label.</p>
    <p style="margin-top:9px;">Cultivated and manufactured in<br>Switzerland.</p>
  </div>

  <!-- Fold guides -->
  <div class="fold-guide" style="left:535px;"></div>
  <div class="fold-guide" style="left:876px;"></div>

</body>
</html>
```